Make a medical leaflet for my patients undergoing ankle blocks

I have a very boring text only leaflet I would like to turn into a professional appealing medical leaflet to give to my patients. I would like to get this onto two pages of a4 if possible and its intended for electronic distribution mainly.
This will be for patients so it must be professional.
It must also contain a copyright logo on it and my name near the start (Dr Tobias Wendell) so my colleagues can't use it easily.
Target Market(s)
Patients undergoing surgery
Industry/Entity Type
Medical
Font styles to use
Other font styles liked:
- no idea, you tell me
Requirements
Must have
- the information contained on the attachment
- look professional
- a copyright on it
Nice to have
- the ashbury clinic logo
Should not have
- Any spelling, grammatical or linguistic errors
- Any font less than size 12

```html
<!DOCTYPE html>
<html lang="en">
<head>
<meta charset="utf-8">
<title>Undergoing Ankle Blocks – Patient Leaflet</title>
<link rel="stylesheet" href="https://fonts.googleapis.com/css2?family=Raleway:wght@400;500;600;700;800&display=swap">
<style>
:root{
  --backdrop:#5e5f61;
  --paper:#ffffff;
  --brand:#1f5ea8;
  --brand-dark:#183f7a;
  --ink:#2a2a2a;
  --muted:#555;
  --rule:#c9ccd2;
  --photo-blue:#7ea6d8;
}
*{box-sizing:border-box;margin:0;padding:0}
html,body{width:1200px;height:874px;overflow:hidden;background:var(--backdrop)}
body{position:relative;font-family:"Raleway",Arial,sans-serif;color:var(--ink)}
.page{position:absolute;top:56px;width:543px;height:765px;background:var(--paper);overflow:hidden}
.page--front{left:45px}
.page--back{left:621px}
.abs{position:absolute}
.bottom-bar{left:0;bottom:0;width:100%;height:13px;background:var(--brand)}

/* identity */
.hospital-name{font-size:24px;font-weight:500;color:var(--brand-dark);letter-spacing:.2px}
.hospital-rule{height:1px;background:var(--brand-dark)}
.hospital-sub{font-size:11px;font-weight:500;color:var(--brand-dark)}
.clinic-box{left:394px;top:0;width:125px;height:122px;background:var(--brand);color:#fff;
  display:flex;flex-direction:column;align-items:center;justify-content:center;text-align:center;
  font-size:14px;letter-spacing:4px;line-height:1.45;font-weight:400}
.name-band{left:0;top:98px;width:287px;height:23px;background:var(--brand);
  clip-path:polygon(0 0,96% 0,100% 100%,0 100%);color:#fff;font-size:14px;font-weight:600;
  padding-left:65px;line-height:23px;letter-spacing:.3px}
.photo{background:linear-gradient(135deg,#eef3f9 0%,var(--photo-blue) 45%,#e9d6c8 80%,#fff 100%)}
.photo--hand{background:radial-gradient(ellipse at 45% 55%,#e8cdb9 0%,#f1e6de 35%,#f6f8fb 70%,#fff 100%)}

/* type */
.title{font-size:18.5px;font-weight:800;color:var(--brand)}
.body{font-size:8.6px;line-height:11.6px;color:var(--ink);text-align:justify}
.body p+p{margin-top:4px}
.sub-head{font-size:10px;font-weight:700;color:var(--brand);text-align:center;width:100%;left:0}
.pill{background:var(--brand);color:#fff;font-size:11.5px;font-weight:700;border-radius:12px;
  height:23px;line-height:23px;padding:0 13px;white-space:nowrap}
.hline{height:1px;background:var(--brand)}
.center{text-align:center}

/* boxes */
.frame-box{border:1.3px solid var(--brand);border-radius:12px}
.benefit-list{list-style:none;font-size:8.6px;line-height:15.5px;text-align:center;padding-top:20px}
.benefit-list svg{width:9px;height:9px;vertical-align:-1px;margin-right:5px}

/* table */
.risk-table{left:26px;top:533px;width:494px;border-collapse:collapse;table-layout:fixed;font-size:8.6px;line-height:11.8px}
.risk-table td{border:1px solid var(--rule);vertical-align:top;padding:4px 8px 2px}
.risk-table .label{width:162px;font-size:9.5px;font-weight:700;color:var(--brand);padding-left:8px}
.risk-table .dash{padding-left:8px;text-indent:-8px}

.cta{font-size:11.3px;font-weight:700;color:var(--brand);line-height:14px;text-align:center}
.links{font-size:10.5px;font-weight:700;color:var(--brand-dark);line-height:17px;text-align:center}
.doctor-name{font-size:18px;font-weight:700;color:var(--brand)}
.vdivider{width:1px;background:var(--rule)}
</style>
</head>
<body>

<section class="page page--front">
  <div class="abs hospital-name" style="left:26px;top:22px">Riverside Gate Hospital</div>
  <div class="abs hospital-rule" style="left:26px;top:54px;width:236px"></div>
  <div class="abs hospital-sub" style="left:48px;top:63px">part of Meridian Health UK</div>

  <div class="abs clinic-box"><span>THE</span><span>ASHBURY</span><span>CLINIC</span></div>
  <div class="abs name-band">DR TOBIAS WENDELL</div>

  <div class="abs photo" style="left:0;top:122px;width:239px;height:222px" role="img" aria-label="Photograph of a foot wearing an ankle support with a blue X-ray overlay of the ankle bones"></div>

  <h1 class="abs title" style="left:248px;top:140px">UNDERGOING ANKLE BLOCKS</h1>
  <div class="abs body" style="left:249px;top:170px;width:271px">
    <p>You are scheduled to have surgery on your foot. It is my normal practice to offer and perform (with your consent) an ankle block. This is an optional injection of numbing liquid to the nerves which supply your foot. The ankle block can be performed when you are awake, sedated or under general anaesthesia.</p>
    <p>The ankle block can be combined with a general anaesthetic and with sedation. It can also be used to allow surgery to be performed with you wide awake in certain cases.</p>
    <p>Having or not having an ankle block does not change the pre operative fasting guidelines you have been given.</p>
    <p>There is a fee for performing an ankle block. Please consult my initial introductory email and terms of business for details</p>
  </div>

  <div class="abs frame-box" style="left:38px;top:362px;width:466px;height:102px">
    <ul class="benefit-list">
      <li><svg viewBox="0 0 10 10"><circle cx="5" cy="5" r="4.3" fill="none" stroke="#1f5ea8" stroke-width="1"/><path d="M2.8 5.2l1.6 1.6 3.4-4" fill="none" stroke="#1f5ea8" stroke-width="1.2"/></svg>Excellent pain relief - usually 10 - 14 hours (and rarely 24 - 48 hours)</li>
      <li><svg viewBox="0 0 10 10"><circle cx="5" cy="5" r="4.3" fill="none" stroke="#1f5ea8" stroke-width="1"/><path d="M2.8 5.2l1.6 1.6 3.4-4" fill="none" stroke="#1f5ea8" stroke-width="1.2"/></svg>Avoiding traditional painkillers which results in less post operative nausea and vomiting</li>
      <li><svg viewBox="0 0 10 10"><circle cx="5" cy="5" r="4.3" fill="none" stroke="#1f5ea8" stroke-width="1"/><path d="M2.8 5.2l1.6 1.6 3.4-4" fill="none" stroke="#1f5ea8" stroke-width="1.2"/></svg>The option to avoid a general anaesthetic (if you wish)</li>
      <li><svg viewBox="0 0 10 10"><circle cx="5" cy="5" r="4.3" fill="none" stroke="#1f5ea8" stroke-width="1"/><path d="M2.8 5.2l1.6 1.6 3.4-4" fill="none" stroke="#1f5ea8" stroke-width="1.2"/></svg>A faster recovery from the general anaesthetic</li>
      <li><svg viewBox="0 0 10 10"><circle cx="5" cy="5" r="4.3" fill="none" stroke="#1f5ea8" stroke-width="1"/><path d="M2.8 5.2l1.6 1.6 3.4-4" fill="none" stroke="#1f5ea8" stroke-width="1.2"/></svg>Certain surgery requires an overnight stay in hospital without an ankle block</li>
    </ul>
  </div>
  <div class="abs pill" style="left:185px;top:352px">WHAT ARE THE BENEFITS</div>

  <div class="abs hline" style="left:147px;top:492px;width:250px"></div>
  <div class="abs pill" style="left:190px;top:481px">WHAT ARE THE RISKS?</div>
  <div class="abs body center" style="left:0;top:515px;width:543px">As with all injections, there is the risk of bruising, bleeding and infection.</div>

  <table class="abs risk-table">
    <tr style="height:67px">
      <td class="label">NERVE DAMAGE</td>
      <td>Occurs 1 in 5000 nerve blocks.<br>Creates an area of numbness or weakness/paralysis in some / all the foot.<br>Majority of nerve injuries will heal themselves within a year<br>There is no treatment to fix it<br>If the block has not worn off after 72 hours please let me know.</td>
    </tr>
    <tr style="height:44px">
      <td class="label">FAILURE</td>
      <td>The success rate with ankle blocks is 98 - 99%<br>Some blocks will fail, partially or totally.<br>If total failure, I will discuss repeating the block with your consent.</td>
    </tr>
    <tr style="height:65px">
      <td class="label">PAIN DURING OPERATION</td>
      <td>If you choose to have wide awake surgery or surgery under sedation<br>The surgery will stop and I will discuss three options with you
        <div class="dash">- &nbsp;more numbing liquid to be injected by the surgeon</div>
        <div class="dash">- &nbsp;more sedation / painkiller</div>
        <div class="dash">- &nbsp;having a general anaesthetic</div></td>
    </tr>
  </table>

  <div class="abs body center" style="left:30px;top:719px;width:483px">If you decide to undergo surgery awake or sedated, there is a risk you will need to have a general anaesthetic if you feel pain. This is why the starvation instructions of awake surgery and general anaesthesia are the same.</div>
  <div class="abs bottom-bar"></div>
</section>

<section class="page page--back">
  <div class="abs hline" style="left:146px;top:37px;width:250px"></div>
  <div class="abs pill" style="left:203px;top:26px">HOW IS IT DONE</div>

  <div class="abs sub-head" style="top:64px">IF YOU CHOOSE AWAKE SURGERY OR SURGERY WITH SEDATION</div>
  <div class="abs body" style="left:31px;top:80px;width:486px;text-align-last:center">Numbing liquid is injected around the nerves which supply your foot. The ankle block takes 5 - 10 minutes to perform and requires 4 - 5 injections. Approximately 10 - 20 minutes to make your foot numb to pain. I will check the ankle block is working before we start surgery using cold spray. Sensations of touch, pressure, vibration and movement will still be felt. I will use a screen so you can't see the surgery (unless you would like to see). Some patients bring headphones to block out the noise of the operation.</div>

  <div class="abs sub-head" style="top:157px">IF YOU CHOOSE A GENERAL ANAESTHETIC</div>
  <div class="abs body" style="left:31px;top:173px;width:486px;text-align-last:center">I will perform the ankle block after I start the general anaesthetic. You should wake up from your surgery with a comfortable and numb foot/feet. If you wake in pain, we can repeat the ankle block or provide traditional painkillers</div>
  <div class="abs body" style="left:31px;top:208px;width:486px">Whatever you choose, there will be a cannula placed in your hand and heart and oxygen monitoring throughout.</div>

  <div class="abs photo photo--hand" style="left:0;top:240px;width:211px;height:256px" role="img" aria-label="Photograph of a doctor's hand giving a thumbs up"></div>

  <div class="abs hline" style="left:218px;top:249px;width:301px"></div>
  <div class="abs pill" style="left:218px;top:238px">AFTER SURGERY</div>

  <div class="abs body" style="left:218px;top:273px;width:299px">
    <p>You will go to the recovery area and then onto the ward when you are ready. It will be difficult to walk while the block is working so physiotherapists will help you first walk. If you need crutches they will teach you how to use them.</p>
    <p>Your foot will be numb and so you will not feel where your foot is in relation to nearby objects. As a result, it is easy to knock your foot. Please take extra care while your foot is still numb.</p>
    <p>As the block wears off, the foot may feel slightly painful, tingly or hot. At this point you should take your painkillers I have prescribed. Depending on your medical history you will have up to three painkillers. I would suggest to start with all three. You will also have an anti - sickness prescribed if one of the painkillers (typically codeine or morphine) makes you feel sick.</p>
    <p>Occasionally, pain after the ankle block wears off will be significant. Please either contact the surgeon's secretary or myself and we can discuss the pain relief options.</p>
  </div>

  <div class="abs frame-box" style="left:38px;top:496px;width:465px;height:62px"></div>
  <div class="abs pill" style="left:205px;top:485px">THE ALTERNATIVE</div>
  <div class="abs body center" style="left:38px;top:514px;width:465px">If you do not have an ankle block your surgery can still proceed.<br>Post operative pain can be managed with traditional painkillers.<br>However, you are more likely to need an overnight stay or feel sick after the anaesthetic.</div>

  <div class="abs cta" style="left:31px;top:569px;width:484px">If you have any further questions about an ankle block I will see you the day of your surgery. Alternatively, you can request the following optional services (as mentioned in my terms of business).</div>
  <div class="abs links" style="left:0;top:622px;width:543px">Email me your Questions<br>Request a Pre operative telephone call<br>Have a clinic appointment</div>

  <div class="abs hospital-name" style="left:24px;top:692px;font-size:20px">Riverside Gate Hospital</div>
  <div class="abs hospital-rule" style="left:24px;top:719px;width:200px"></div>
  <div class="abs hospital-sub" style="left:42px;top:726px;font-size:10px">part of Meridian Health UK</div>
  <div class="abs vdivider" style="left:281px;top:690px;height:54px"></div>
  <div class="abs doctor-name" style="right:24px;top:707px">DR TOBIAS WENDELL</div>

  <div class="abs bottom-bar"></div>
</section>

</body>
</html>
```